"Eyebrow Threading Flyer Design"

We need a flyer design for a new service that will be provided in our established Beauty Salon in Toorak called "Threading". We provide all beauty services for our clients & would like to now introduce this very popular ancient method of hair removal.
Following are four "40% Off Threading Combo Packages" that will hopefully tempt new clients into our salon.
#Package 1- Eyebrow Threading plus Eyebrow Tint or Eyelash Tint Normally $53 Now $32
#Package 2- Eyebrow Threading plus Full Set Mink Lash Extensions
Normally $208 Now $125
#Package 3- Eyebrow Threading plus Glossine Manicure Or Pedicure
Normally $128 Now $77
#Package 4- Eyebrow Threading plus Collagen Facial
Normally $148 Now $89
We would like to see designs that use pink with whit or black to suit logo & business name & final design should be girly/feminine 7 fun.
On the back we would like the following details:
Velvet Daisy Beauty, "Marlowe Court", shop 7, 846 Brindle Street, 3917
Tel: 03 9471 3629, Email: info@velvetdaisybeauty.example, Web: www.velvetdaisybeauty.example
A map of exact location and business hours:
Mon 9am to 5pm, Tue 9am to 6pm, Wed 9am to 6pm, Thu 9am to 8pm, Fri 9am to 6pm, sat 9am to 5pm

Target Market(s)

Women between the ages of 20 to 60 years of age

Industry/Entity Type

Hair

Font styles to use
Script

Colors
e34297
000000

Requirements
Must have
• Pink and black or pink and white colors
Should not have
• Fake looking eyelashes displayed

```html
<!DOCTYPE html>
<html lang="en">
<head>
<meta charset="utf-8">
<title>Velvet Daisy Beauty – Threading Flyer</title>
<link rel="stylesheet" href="https://fonts.googleapis.com/css2?family=Tinos:wght@400;700&family=Arimo:wght@700&family=Archivo+Black&family=Cousine&display=swap">
<style>
  :root{
    --pink:#e5007d;
    --pink-soft:#e34297;
    --black:#000;
    --white:#fff;
    --paper:#f4f4f4;
    --grey:#9a9a9a;
    --label:#666;
    --panel-w:458px;
    --panel-h:990px;
  }
  *{box-sizing:border-box;margin:0;padding:0}
  html,body{width:1063px;height:1200px;overflow:hidden;background:var(--white)}
  body{position:relative;font-family:"Arimo",Arial,sans-serif}

  .side-label{position:absolute;top:88px;font-family:"Cousine",monospace;font-size:18px;color:var(--label)}
  .side-label.front{left:47px}
  .side-label.back{left:563px}

  .flyer{position:absolute;top:120px;width:var(--panel-w);height:var(--panel-h);border:1px solid #333;overflow:hidden;
    background:linear-gradient(135deg,#5a5a5a 0%,#1a1a1a 35%,#3c3c3c 55%,#0d0d0d 80%,#444 100%)}
  .flyer.front{left:47px}
  .flyer.back{left:563px}

  .texture{position:absolute;inset:0}
  .header{position:absolute;left:0;top:0;width:100%;height:280px}
  .header svg{position:absolute;inset:0}
  .crest-mark{position:absolute;left:50%;top:28px;width:120px;height:120px;margin-left:-60px;border:3px solid #b5b5b5;border-radius:50%}
  .brand{position:absolute;left:0;right:0;top:188px;text-align:center;font-family:"Tinos",serif;font-weight:700;color:var(--pink);line-height:1}
  .brand .name{display:block;font-size:38px;letter-spacing:0.5px}
  .brand .sub{display:block;font-size:21px;letter-spacing:5px;margin-top:4px}

  .offer-badge{position:absolute;left:20px;top:230px;width:170px;height:170px;border-radius:50%;
    background:var(--black);border:5px solid var(--white);box-shadow:6px 6px 0 var(--pink);
    display:flex;align-items:center;justify-content:center;text-align:center;
    font-family:"Tinos",serif;font-weight:700;color:var(--white);font-size:24px;line-height:1.06}

  .package{position:absolute;left:0;width:100%}
  .package h2{font-family:"Archivo Black",sans-serif;font-weight:400;font-size:25px;color:var(--white);letter-spacing:1.5px;
    text-shadow:-2px -2px 0 #000,2px -2px 0 #000,-2px 2px 0 #000,2px 2px 0 #000,0 2px 0 #000}
  .package .band{background:var(--pink);color:var(--white);font-size:18px;line-height:1.45;padding:6px 12px 6px 26px;letter-spacing:.3px}
  .package .price{font-family:"Archivo Black",sans-serif;font-size:26px;color:var(--black);margin-left:4px}

  .pkg-1{top:330px;transform:rotate(-7deg);transform-origin:right bottom}
  .pkg-1 h2{text-align:right;padding-right:50px}
  .pkg-1 .band{padding-top:10px;padding-bottom:8px;margin-left:-10px;width:460px}
  .pkg-2{top:478px}
  .pkg-2 h2{text-align:right;padding-right:22px}
  .pkg-2 .band{padding-left:26px}
  .pkg-3{top:576px;transform:rotate(-3deg)}
  .pkg-3 h2{padding-left:26px}
  .pkg-3 .band{margin-top:2px}
  .pkg-4{top:678px}
  .pkg-4 h2{text-align:right;padding-right:22px}

  .photo{position:absolute;left:0;width:100%}
  .front .photo{top:768px;height:222px;background:linear-gradient(100deg,#e9d6cc 0%,#f2e4dc 40%,#d9c1b4 70%,#c9c9c9 100%)}
  .back .photo{top:831px;height:159px;background:linear-gradient(90deg,#e8d2c4 0%,#f4ece8 45%,#f7f2f4 75%,#e9c6dc 100%)}
  .pink-rule{position:absolute;left:0;top:824px;width:100%;height:6px;background:var(--pink)}

  .map{position:absolute;left:25px;top:298px;width:400px;height:272px;border:6px solid var(--pink);
    background:linear-gradient(160deg,#ecebe6,#e0ddd5);box-shadow:0 0 0 2px #000}
  .map .pin{position:absolute;left:166px;top:102px;width:10px;height:10px;border-radius:50%;background:var(--pink)}

  .hours{position:absolute;left:22px;top:583px;right:14px;font-family:"Arimo",sans-serif;font-weight:700;font-size:18.5px;line-height:19px;color:var(--white);
    text-shadow:-1.5px -1.5px 0 #000,1.5px -1.5px 0 #000,-1.5px 1.5px 0 #000,1.5px 1.5px 0 #000;white-space:pre}

  .contact{position:absolute;left:25px;top:659px;width:400px;height:150px;background:var(--black);border:1px solid #555;
    text-align:center;font-family:"Tinos",serif;color:var(--white);font-size:21px;line-height:25px;padding-top:12px}
  .contact .link{color:var(--pink);font-weight:700}
</style>
</head>
<body>
  <span class="side-label front">front</span>
  <span class="side-label back">back</span>

  <section class="flyer front">
    <div class="texture" role="img" aria-label="Dark glossy hexagonal tile pattern background"></div>
    <div class="header">
      <svg width="458" height="280" viewBox="0 0 458 280"><defs><linearGradient id="paperA" x1="0" y1="0" x2="0" y2="1"><stop offset="0" stop-color="#f7f7f7"/><stop offset="1" stop-color="#ececec"/></linearGradient></defs><path d="M0 0H458V198Q229 340 0 198Z" fill="url(#paperA)"/></svg>
      <span class="crest-mark"></span>
      <p class="brand"><span class="name">VELVET DAISY</span><span class="sub">BEAUTY</span></p>
    </div>

    <div class="offer-badge">40% OFF<br>Threading<br>Combo<br>Packages</div>

    <article class="package pkg-1">
      <h2>PACKAGE 1</h2>
      <p class="band">Eyebrow Threading plus Eyebrow Tint<br>or Eyelash Tint Normally $53 NOW <span class="price">$32</span></p>
    </article>
    <article class="package pkg-2">
      <h2>PACKAGE 2</h2>
      <p class="band">Eyebrow Threading plus Full Set Mink Lash<br>Extensions Normally $208 NOW <span class="price">$125</span></p>
    </article>
    <article class="package pkg-3">
      <h2>PACKAGE 3</h2>
      <p class="band">Eyebrow Threading plus Glossine Manicure<br>Or Pedicure Normally $128 NOW <span class="price">$77</span></p>
    </article>
    <article class="package pkg-4">
      <h2>PACKAGE 4</h2>
      <p class="band">Eyebrow Threading plus Collagen Facial<br>Normally $148 NOW <span class="price">$89</span></p>
    </article>

    <div class="photo" role="img" aria-label="Photo of a woman having her eyebrows shaped with thread"></div>
  </section>

  <section class="flyer back">
    <div class="texture" role="img" aria-label="Dark glossy hexagonal tile pattern background"></div>
    <div class="header">
      <svg width="458" height="280" viewBox="0 0 458 280"><defs><linearGradient id="paperB" x1="0" y1="0" x2="0" y2="1"><stop offset="0" stop-color="#f7f7f7"/><stop offset="1" stop-color="#ececec"/></linearGradient></defs><path d="M0 0H458V198Q229 340 0 198Z" fill="url(#paperB)"/></svg>
      <span class="crest-mark"></span>
      <p class="brand"><span class="name">VELVET DAISY</span><span class="sub">BEAUTY</span></p>
    </div>

    <div class="map" role="img" aria-label="Street map showing the salon location"><span class="pin"></span></div>

    <p class="hours">Mon  9AM to 5PM - Tue 9AM to 6PM
Wed  9AM to 6PM - Thu 9AM to 8PM
Fri     9AM to 6PM - Sat  9AM to 5PM</p>

    <address class="contact" style="font-style:normal">
      Velvet Daisy Beauty, "Marlowe Court",<br>
      shop 7, 846 Brindle Street, 3917<br>
      Tel: 03 9471 3629,<br>
      <span class="link">Email: info@velvetdaisybeauty.example</span><br>
      <span class="link">Web: www.velvetdaisybeauty.example</span>
    </address>

    <div class="pink-rule"></div>
    <div class="photo" role="img" aria-label="Photo of pedicured feet on a white towel with pink orchids"></div>
  </section>
</body>
</html>
```